Price Calculator as Responsive Web App to support Sales People

We need to build a simple micro web app to support sales people in making quotes. We already have a backend that can take a number of parameters and create a quote. We need put a responsive web app on top of this so that our people on the road can easily do their price simulations.

We need two pages. One for the input and another for the results. No menus, navigations, etc. It is 6 different inputs as shown with boxes in the sketch. They don't need to be boxed, but some of them have a bit of instruction text that clearly need to belong to the input.

This needs to be responsive, but first and foremost designed for smartphones. I have included a background gradient that we would like to use -- or a variant of it. We expect this to be delivered as HTML/CSS + images so that we can quickly write a few pieces of JavaScript ourselves to wire it up to our price simulator.

Industry/Entity Type

Information Technology

Coding

Coded - Design and coding required

Number of Pages Required

2 page

Font styles to use
Sans Serif

Requirements
Must have
• Responsive design
• Easy to wire up JavaScript to the HTML/CSS
Nice to have
• Some quick way to pick number of months. +/- buttons to add remove a year or 3 months. Same thing with number of items. Add 10 or 5 quickly.
• Maybe some parallax effect while scrolling as long as it is not distracting.
Should not have
• Toolbars, Menus, Navigations, Banners, etc. This is just a single micro app.

```html
<!DOCTYPE html>
<html lang="en">
<head>
<meta charset="utf-8">
<title>Engine Power Form</title>
<link rel="stylesheet" href="https://fonts.googleapis.com/css2?family=Saira:wght@400;500&family=Lato:wght@400;700;900&display=swap">
<style>
  :root{
    --bg-center:#0f3d63;
    --bg-edge:#021a33;
    --panel:rgba(30,70,105,0.55);
    --panel-line:rgba(120,160,200,0.18);
    --band:rgba(10,30,52,0.45);
    --band-dark:rgba(6,20,38,0.55);
    --selected:#0e2640;
    --value-box:#0b2036;
    --btn:rgba(255,255,255,0.04);
    --btn-active:#2a4865;
    --btn-border:rgba(255,255,255,0.16);
    --text:#ffffff;
    --text-soft:#e4ecf4;
    --rule:rgba(255,255,255,0.45);
    --submit:#1f66ad;
    --submit-arrow:#7aa3cb;
    --footer:#000000;
  }
  *{box-sizing:border-box;margin:0;padding:0}
  html,body{width:993px;height:1200px;overflow:hidden}
  body{
    position:relative;
    background:radial-gradient(ellipse 70% 60% at 50% 45%,var(--bg-center) 0%,#0a2d4d 55%,var(--bg-edge) 100%);
    color:var(--text);
    font-family:'Saira',sans-serif;
  }
  .page-title{
    position:absolute;top:18px;left:0;width:100%;
    text-align:center;font-weight:400;font-size:30px;letter-spacing:0.5px;
  }
  .title-rule{position:absolute;top:60px;left:329px;width:336px;height:16px}
  .form-panel{
    position:absolute;left:67px;top:104px;width:859px;height:1010px;
    background:var(--panel);border:1px solid var(--panel-line);
  }
  .section-label{
    position:absolute;left:15px;height:24px;line-height:24px;
    font-size:19px;font-weight:400;letter-spacing:0.2px;text-transform:uppercase;
  }
  .row{position:absolute;left:0;right:0;height:60px;background:var(--band)}
  .step-btn{
    position:absolute;top:6px;width:58px;height:47px;
    border:1px solid var(--btn-border);background:var(--btn);
    color:var(--text);font-family:'Saira',sans-serif;font-size:20px;
    display:flex;align-items:center;justify-content:center;
  }
  .step-btn.is-active{background:var(--btn-active);border-color:var(--btn-active)}
  .step-value{
    position:absolute;left:227px;top:0;width:58px;height:60px;
    background:var(--value-box);font-family:'Lato',sans-serif;font-weight:900;font-size:22px;
    display:flex;align-items:center;justify-content:center;letter-spacing:0.5px;
  }
  .step-unit{position:absolute;left:301px;top:0;height:60px;line-height:60px;font-size:16px}
  .radio{
    position:absolute;display:flex;align-items:center;gap:17px;
    font-size:17px;color:var(--text-soft);white-space:nowrap;
  }
  .radio-dot{
    width:21px;height:21px;border:1.5px solid #fff;border-radius:50%;
    display:flex;align-items:center;justify-content:center;flex:none;
  }
  .radio.is-checked .radio-dot::after{
    content:"";width:11px;height:11px;border-radius:50%;background:#fff;
  }
  .radio.is-checked{font-family:'Lato',sans-serif;font-weight:700;color:#fff;letter-spacing:0.6px}
  .plan-block{position:absolute;left:0;right:0;top:306px;height:224px;background:var(--band)}
  .plan-selected{position:absolute;left:0;right:0;top:60px;height:42px;background:var(--selected)}
  .plan-price{display:inline-block;width:106px}
  .plan-dash{display:inline-block;width:20px}
  .notice{
    position:absolute;left:27px;top:193px;font-family:'Lato',sans-serif;
    font-size:13.5px;color:var(--text-soft);white-space:nowrap;
  }
  .notice strong{font-weight:700;color:#fff}
  .cell-selected{position:absolute;top:0;left:178px;width:147px;height:60px;background:var(--selected)}
  .choice-row .radio{top:19px}
  .submit-btn{
    position:absolute;left:7px;top:950px;width:134px;height:37px;
    background:var(--submit);display:flex;align-items:center;
    border:1px solid rgba(255,255,255,0.12);
  }
  .submit-label{flex:1;padding-left:10px;font-family:'Lato',sans-serif;font-weight:900;font-size:21px;letter-spacing:0.3px}
  .submit-arrow{width:33px;height:31px;margin-right:3px;background:var(--submit-arrow);display:flex;align-items:center;justify-content:center}
  .site-footer{
    position:absolute;left:0;bottom:0;width:100%;height:49px;background:var(--footer);
    font-family:'Lato',sans-serif;font-size:11.5px;color:#e8e8e8;
    display:flex;align-items:center;justify-content:center;gap:8px;
  }
</style>
</head>
<body>
  <h1 class="page-title">ENGINE POWER FORM</h1>
  <svg class="title-rule" viewBox="0 0 336 16" aria-hidden="true">
    <line x1="0" y1="8" x2="137" y2="8" stroke="rgba(255,255,255,0.45)" stroke-width="1"/>
    <line x1="199" y1="8" x2="336" y2="8" stroke="rgba(255,255,255,0.45)" stroke-width="1"/>
    <g fill="#fff">
      <polygon points="151,2 152.8,6.2 157.2,6.4 153.8,9.2 155,13.5 151,11 147,13.5 148.2,9.2 144.8,6.4 149.2,6.2"/>
      <polygon points="168,2 169.8,6.2 174.2,6.4 170.8,9.2 172,13.5 168,11 164,13.5 165.2,9.2 161.8,6.4 166.2,6.2"/>
      <polygon points="185,2 186.8,6.2 191.2,6.4 187.8,9.2 189,13.5 185,11 181,13.5 182.2,9.2 178.8,6.4 183.2,6.2"/>
    </g>
  </svg>

  <form class="form-panel">
    <div class="section-label" style="top:13px">Duration</div>
    <div class="row stepper" style="top:51px">
      <div class="step-btn is-active" style="left:10px">-1</div>
      <div class="step-btn" style="left:102px">-12</div>
      <div class="step-value">24</div>
      <div class="step-unit">MONTH</div>
      <div class="step-btn" style="left:415px">+1</div>
      <div class="step-btn" style="left:506px">+12</div>
    </div>

    <div class="section-label" style="top:137px">Count</div>
    <div class="row stepper" style="top:173px">
      <div class="step-btn is-active" style="left:10px">-1</div>
      <div class="step-btn" style="left:102px">-10</div>
      <div class="step-value">100</div>
      <div class="step-unit">ITEMS</div>
      <div class="step-btn" style="left:415px">+1</div>
      <div class="step-btn" style="left:506px">+10</div>
    </div>

    <div class="section-label" style="top:267px">Engine Power (Beyond Standard)</div>
    <div class="plan-block">
      <div class="plan-selected"></div>
      <div class="radio" style="left:24px;top:24px"><span class="radio-dot"></span><span><span class="plan-price">360 $ / Year</span><span class="plan-dash">-</span>Bounce Power</span></div>
      <div class="radio is-checked" style="left:24px;top:70px"><span class="radio-dot"></span><span>600 $ / Year - Silver Power</span></div>
      <div class="radio" style="left:24px;top:113px"><span class="radio-dot"></span><span><span class="plan-price">1M $ / Year</span><span class="plan-dash">-</span>Gold Power</span></div>
      <div class="radio" style="left:24px;top:152px"><span class="radio-dot"></span><span><span class="plan-price">3M $ / Year</span><span class="plan-dash">-</span>Platinum Power</span></div>
      <p class="notice"><strong>Notic :</strong> Lorem ipsum dolor sit amet consectetuer adipiscing elit sed diam nonummy nibh euismod tincidunt ut laoreet lorem ipsum</p>
    </div>

    <div class="section-label" style="top:569px">Shared Storage Addition</div>
    <div class="row choice-row" style="top:606px">
      <div class="cell-selected"></div>
      <div class="radio" style="left:24px"><span class="radio-dot"></span>10 Kg</div>
      <div class="radio is-checked" style="left:207px"><span class="radio-dot"></span>50 Kg</div>
      <div class="radio" style="left:391px"><span class="radio-dot"></span>100 Kg</div>
      <div class="radio" style="left:583px"><span class="radio-dot"></span>500Kg</div>
      <div class="radio" style="left:774px"><span class="radio-dot"></span>1T</div>
    </div>

    <div class="section-label" style="top:700px">Additional Tip</div>
    <div class="row choice-row" style="top:733px">
      <div class="cell-selected"></div>
      <div class="radio" style="left:24px"><span class="radio-dot"></span>15 %</div>
      <div class="radio is-checked" style="left:207px"><span class="radio-dot"></span>18 %</div>
      <div class="radio" style="left:391px"><span class="radio-dot"></span>20 %</div>
    </div>

    <div class="section-label" style="top:828px">Elastic Extension</div>
    <div class="row choice-row" style="top:864px">
      <div class="cell-selected"></div>
      <div class="radio" style="left:24px"><span class="radio-dot"></span>30 %</div>
      <div class="radio is-checked" style="left:207px"><span class="radio-dot"></span>50 %</div>
    </div>

    <div class="submit-btn" role="button">
      <span class="submit-label">SUBMIT</span>
      <span class="submit-arrow"><svg width="10" height="13" viewBox="0 0 10 13" aria-hidden="true"><polygon points="0,0 10,6.5 0,13" fill="#fff"/></svg></span>
    </div>
  </form>

  <footer class="site-footer"><span>© 2017 ENGINE POWER FORM</span><span>|</span><span>All rights reserved</span></footer>
</body>
</html>
```